Managed Service Provider need new business cards

We are a small Maanged Service Provider of IT Services and need a new fresh design for our business cards. We want something impossible, fun and professional :)
Our services has a large range, but we are always fun and make sure our customers both get their issue sorted and also feel like they are "catching up with an old friend".
All our cards in the past has always been all black, with red and we need something fresher.
The back of card, we would like just a small list of what we do i think, but if someone has a better idea, please do something cool with the back of the card:
Managed IT Services
Productivity Solutions
Data Backup and Recovery
IT System Maintenance
Managed IT Security
More details can be found on our website tqnetworks.com.au
Industry/Entity Type
It Company
Contact Information for Business Card
Name: Dwayne Falstrup
Title: Director
Phone: 03 6193 4827
Mobile: 0412 587 239
Email: dwayne@tqnetworks.com.au
Web: www.tqnetworks.com.au

```html
<!DOCTYPE html>
<html lang="en">
<head>
<meta charset="utf-8">
<title>TQ Networks – Business Cards</title>
<link rel="stylesheet" href="https://fonts.googleapis.com/css2?family=Oswald:wght@600&family=Arimo:wght@400;700&display=swap">
<style>
  :root {
    --backdrop: #2a2624;
    --card: #0c0c0c;
    --red: #ed1c24;
    --white: #f2f2f2;
    --grey: #c9c9c9;
    --rule: #3a3a3a;
  }
  * { box-sizing: border-box; margin: 0; padding: 0; }
  html, body { width: 1200px; height: 842px; overflow: hidden; }
  body {
    background: var(--backdrop);
    font-family: "Arimo", Arial, sans-serif;
    position: relative;
  }
  .card {
    position: absolute;
    top: 256px;
    width: 540px;
    height: 330px;
    background: var(--card);
    box-shadow: 0 10px 30px rgba(0,0,0,.55);
    overflow: hidden;
  }
  .card--front { left: 40px; }
  .card--back { left: 620px; }

  .band { position: absolute; left: 0; right: 0; height: 12px; background: var(--red); }
  .band--top { top: 0; }
  .band--bottom { bottom: 0; }

  .contact {
    position: absolute;
    left: 0; right: 0; top: 92px;
    text-align: center;
  }
  .contact__name {
    font-family: "Oswald", "Arial Narrow", sans-serif;
    font-weight: 600;
    font-size: 27px;
    letter-spacing: .5px;
    text-transform: uppercase;
    color: var(--red);
    line-height: 1.05;
  }
  .contact__title { font-size: 15px; color: var(--grey); margin-top: 2px; }
  .contact__rule { width: 210px; height: 1px; background: var(--rule); margin: 14px auto 12px; }
  .contact__line { font-size: 16px; color: var(--grey); line-height: 1.3; }
  .contact__label { color: var(--red); font-weight: 700; }
  .contact__domain { color: var(--red); }

  .tab { position: absolute; width: 42px; height: 34px; background: var(--red); }
  .tab--left { left: 0; top: 96px; }
  .tab--right { right: 0; top: 28px; }

  .brand {
    position: absolute;
    left: 0; right: 0; top: 104px;
    display: flex; align-items: center; justify-content: center; gap: 12px;
  }
  .brand__dot { width: 14px; height: 14px; border-radius: 50%; background: var(--red); }
  .brand__name {
    font-family: "Oswald", "Arial Narrow", sans-serif;
    font-weight: 600;
    font-size: 44px;
    text-transform: uppercase;
    color: var(--red);
    letter-spacing: 1px;
  }
  .services {
    position: absolute;
    left: 0; right: 0; top: 196px;
    text-align: center;
    font-size: 14px;
    color: var(--white);
    line-height: 1.35;
  }
  .services__sep {
    display: inline-block; width: 6px; height: 6px; border-radius: 50%;
    background: var(--red); vertical-align: middle; margin: 0 3px;
  }
</style>
</head>
<body>
  <section class="card card--front">
    <div class="band band--top"></div>
    <div class="contact">
      <h1 class="contact__name">Dwayne Falstrup</h1>
      <p class="contact__title">Director</p>
      <div class="contact__rule"></div>
      <p class="contact__line"><span class="contact__label">P:</span> 03 6193 4827</p>
      <p class="contact__line"><span class="contact__label">M:</span> 0412 587 239</p>
      <p class="contact__line"><span class="contact__label">E:</span> dwayne@tqnetworks.com.au</p>
      <p class="contact__line">www.<span class="contact__domain">tqnetworks</span>.com.au</p>
    </div>
    <div class="band band--bottom"></div>
  </section>

  <section class="card card--back">
    <div class="tab tab--left"></div>
    <div class="tab tab--right"></div>
    <div class="brand">
      <span class="brand__name">TQ Networks</span>
      <span class="brand__dot"></span>
    </div>
    <div class="services">
      <p>Data Backup and Recovery</p>
      <p>IT System Maintenance<span class="services__sep"></span>Productivity Solutions</p>
      <p>Managed IT Security<span class="services__sep"></span>Managed IT Services</p>
    </div>
  </section>
</body>
</html>
```